Rack card for a integrative medical practice

Need an eye-catching rack card with our logo with content as provided. We have a membership based holistic medical practice which incorporates western and holistic medicine. We would like to focus on wellness and healthy lifestyle. See uploaded files for what is included in the membership. Would like 2 page rack card color on both sides. Logo must be on the front.

Target Market(s)

People looking for alternative medicine, healthy lifestyle.

Industry/Entity Type

Health and Wellness

Colors
00AB8E
00BBA5
67D7C9
C6EFE9
E9F9F6

Requirements
Must have
• Must spark interest at first sight. Clear message.
Nice to have
• Warm, bright and positive vibe. Organic, neutral and earthy colors.
Should not have
• Traditional medical practice vibe (cold, formal, industrial). No PINK except the logo.

```html
<!DOCTYPE html>
<html lang="en">
<head>
<meta charset="utf-8">
<title>Willow Health &amp; Wellness — Rack Card</title>
<link href="https://fonts.googleapis.com/css2?family=Manrope:wght@500;600;700;800&display=swap" rel="stylesheet">
<style>
  :root {
    --teal: #0fbba5;
    --teal-deep: #00ab8e;
    --ink: #0f2e2a;
    --white: #ffffff;
    --stage: #58585a;
    --photo-top: #eef1ee;
    --photo-bottom: #cfd6cc;
  }
  * { box-sizing: border-box; margin: 0; padding: 0; }
  html, body {
    width: 813px; height: 1200px; overflow: hidden;
    background: var(--stage);
    font-family: "Manrope", Arial, sans-serif;
  }
  .canvas { position: relative; width: 813px; height: 1200px; }

  .card {
    position: absolute; top: 216px;
    width: 340px; height: 767px;
    background: var(--white);
    overflow: hidden;
    box-shadow: 0 14px 24px rgba(0,0,0,0.35);
  }
  .card--front { left: 36px; }
  .card--back { left: 437px; }

  /* brand name */
  .brand { position: absolute; left: 0; right: 0; text-align: center; color: var(--ink); font-weight: 700; }
  .brand__dot { display: block; width: 30px; height: 30px; border-radius: 50%; background: var(--teal); margin: 0 auto 10px; }
  .brand__name { display: block; font-size: 38px; letter-spacing: 9px; line-height: 1; padding-left: 9px; }
  .brand__tag { display: block; font-size: 10.5px; letter-spacing: 4px; margin-top: 6px; padding-left: 4px; }
  .card--front .brand { top: 48px; }

  /* front */
  .front__band { position: absolute; left: 0; right: 0; top: 361px; bottom: 0; background: var(--teal); }
  .front__photo {
    position: absolute; left: 73px; top: 173px; width: 267px; height: 390px;
    border-top-left-radius: 150px 210px;
    border-bottom-left-radius: 60px 40px;
    background: linear-gradient(180deg, var(--photo-top) 0%, var(--photo-bottom) 100%);
  }
  .front__arcs { position: absolute; inset: 0; }
  .front__badge {
    position: absolute; left: 32px; top: 450px; width: 216px; height: 216px;
    border-radius: 50%; background: var(--white);
    display: flex; align-items: center; justify-content: center;
  }
  .front__badge-ring {
    width: 202px; height: 202px; border-radius: 50%;
    border: 3px solid var(--teal);
    display: flex; align-items: center; justify-content: center; text-align: center;
    color: var(--teal); font-weight: 700; font-size: 16.5px; line-height: 1.3;
    white-space: nowrap;
  }
  .front__rule { position: absolute; left: 25px; right: 25px; top: 690px; height: 2px; background: var(--white); }
  .front__address {
    position: absolute; left: 0; right: 0; top: 708px;
    text-align: center; color: var(--white); font-size: 15px; font-weight: 600; line-height: 1.35;
  }

  /* back */
  .back__title {
    position: absolute; left: 0; right: 0; top: 28px;
    text-align: center; color: var(--teal); font-weight: 800; font-size: 22px; line-height: 1.2;
    text-transform: uppercase; letter-spacing: -0.2px;
  }
  .benefits { position: absolute; left: 27px; top: 100px; width: 290px; list-style: none; }
  .benefit { position: relative; height: 56px; margin-bottom: 9px; }
  .benefit--tall { height: 87px; }
  .benefit__pill {
    position: absolute; left: 20px; right: 0; top: 0; bottom: 0;
    background: var(--teal); border-radius: 16px 12px 12px 16px;
    color: var(--white); font-size: 14.2px; font-weight: 500; line-height: 1.3;
    padding: 0 8px 0 37px; display: flex; align-items: center;
  }
  .benefit__num {
    position: absolute; left: 0; top: 50%; transform: translateY(-50%);
    width: 43px; height: 43px; border-radius: 50%;
    background: var(--white); border: 2.5px solid var(--teal);
    color: var(--teal); font-weight: 700; font-size: 16px;
    display: flex; align-items: center; justify-content: center; z-index: 1;
  }
  .card--back .brand { top: 670px; }
  .card--back .brand__dot { width: 20px; height: 20px; margin-bottom: 6px; }
  .card--back .brand__name { font-size: 22px; letter-spacing: 5px; padding-left: 5px; }
  .card--back .brand__tag { font-size: 6.5px; letter-spacing: 2.4px; margin-top: 4px; }
</style>
</head>
<body>
<main class="canvas">

  <section class="card card--front" aria-label="Rack card front">
    <div class="brand">
      <span class="brand__dot"></span>
      <span class="brand__name">WILLOW</span>
      <span class="brand__tag">HEALTH &amp; WELLNESS</span>
    </div>
    <div class="front__band"></div>
    <div class="front__photo" role="img" aria-label="Photo of a woman meditating cross-legged outdoors beside sheer white curtains"></div>
    <svg class="front__arcs" width="340" height="767" viewBox="0 0 340 767" aria-hidden="true">
      <path d="M55 364 Q51 412 68 452" fill="none" stroke="var(--white)" stroke-width="5" stroke-linecap="round"/>
      <path d="M264 587 Q302 586 340 571" fill="none" stroke="var(--white)" stroke-width="5" stroke-linecap="round"/>
    </svg>
    <div class="front__badge">
      <p class="front__badge-ring">A direct primary<br>care practice<br>Focused on a more<br>holistic And personal<br>approach to<br>Medicine.</p>
    </div>
    <div class="front__rule"></div>
    <p class="front__address">1420 Elm Ridge Rd., STE 2B<br>Fairhaven.</p>
  </section>

  <section class="card card--back" aria-label="Rack card back">
    <h2 class="back__title">What's included in your<br>membership</h2>
    <ol class="benefits">
      <li class="benefit"><span class="benefit__num">01</span><span class="benefit__pill">Unlimited office visits with no copay</span></li>
      <li class="benefit"><span class="benefit__num">02</span><span class="benefit__pill">Direct communication with your doctor</span></li>
      <li class="benefit"><span class="benefit__num">03</span><span class="benefit__pill">Discounted labs, imaging and medications</span></li>
      <li class="benefit"><span class="benefit__num">04</span><span class="benefit__pill">Free initial acupuncture session ($250 value)</span></li>
      <li class="benefit"><span class="benefit__num">05</span><span class="benefit__pill">2 BodyScan testings per year ($100 value)</span></li>
      <li class="benefit"><span class="benefit__num">06</span><span class="benefit__pill">Discounts for supplements and health products in the clinic</span></li>
      <li class="benefit"><span class="benefit__num">07</span><span class="benefit__pill">Discounts for iv vitamin infusion therapy</span></li>
      <li class="benefit benefit--tall"><span class="benefit__num">08</span><span class="benefit__pill">Personalized nutrition plan after advanced testing such as gut microbiome, hormonal, metabolism test, etc.</span></li>
    </ol>
    <div class="brand">
      <span class="brand__dot"></span>
      <span class="brand__name">WILLOW</span>
      <span class="brand__tag">HEALTH &amp; WELLNESS</span>
    </div>
  </section>

</main>
</body>
</html>
```